Professional Financial services company want to rebrand their stationary

We need stationary design for Veltor Group, its a company with 4 member companys that include Veltor Auditing, Veltor Financial Consultancy, Veltor Debt Collection and Veltor Real Estate.

We are based in dubai so the designers need to keep in mind that we use both english and arabic so leave a space for the arabic writing.

We recently redesigned our Logo and would like to redesign our stationary to go along with it.

You will find attached the logo, please keep it looking professional and use the logo as a guide for colors when designing.

Good luck to everyone

Industry/Entity Type

Finance And Accounting

Font styles to use
Sans Serif

Colors
0292cd
33a6d7
3276b5
0355a3
ffffff
dbdbdb

Requirements
Must have
• Letterhead
• Business card
• Envelope small and A4
Nice to have
• Professional
• Space for Arabic and english

```html
<!DOCTYPE html>
<html lang="en">
<head>
<meta charset="utf-8">
<title>Veltor Group – Business Card</title>
<link href="https://fonts.googleapis.com/css2?family=Montserrat:wght@500;600&family=Work+Sans:wght@400;500&display=swap" rel="stylesheet">
<style>
  :root {
    --page-bg: #e9e9e9;
    --card-front: #68696b;
    --card-back: #ffffff;
    --brand-blue: #0a6db8;
    --band-grey: #6f7072;
    --text-dark: #3a3a3a;
    --text-muted: #555555;
    --white: #ffffff;
  }
  * { margin: 0; padding: 0; box-sizing: border-box; }
  html, body {
    width: 1200px; height: 930px; overflow: hidden;
    background: var(--page-bg);
    font-family: "Work Sans", Arial, sans-serif;
  }
  .card {
    position: absolute;
    width: 560px; height: 320px;
    box-shadow: 0 6px 18px rgba(0,0,0,0.18);
    overflow: hidden;
  }
  .brand {
    display: flex; align-items: center; gap: 12px;
    font-family: "Montserrat", Arial, sans-serif;
    font-weight: 600; letter-spacing: 1px; text-transform: uppercase;
    white-space: nowrap;
  }
  .brand__mark { flex: none; }

  /* Front face */
  .card--front { left: 70px; top: 90px; background: var(--card-front); }
  .card--front .brand {
    position: absolute; left: 0; right: 0; top: 130px;
    justify-content: center;
    font-size: 38px; color: var(--white);
  }
  .card--front .brand__mark { width: 22px; height: 22px; background: var(--white); }
  .card--front .website {
    position: absolute; left: 0; right: 0; bottom: 34px;
    text-align: center; color: #e0e0e0; font-size: 13px; letter-spacing: 1px;
  }

  /* Back face */
  .card--back { left: 570px; top: 520px; background: var(--card-back); }
  .card--back .brand {
    position: absolute; left: 36px; top: 168px;
    font-size: 24px; color: var(--brand-blue);
  }
  .card--back .brand__mark { width: 16px; height: 16px; background: var(--brand-blue); }
  .divider {
    position: absolute; left: 296px; top: 60px;
    width: 1.5px; height: 160px; background: var(--brand-blue);
  }
  .contact { position: absolute; left: 318px; top: 50px; }
  .contact__name {
    font-family: "Montserrat", Arial, sans-serif; font-weight: 500;
    font-size: 19px; letter-spacing: 1px; color: var(--brand-blue);
    text-transform: uppercase; white-space: nowrap;
  }
  .contact__role { font-size: 12px; font-weight: 500; color: var(--text-dark); margin-top: 2px; }
  .contact__address { font-size: 12px; color: var(--text-muted); margin-top: 14px; line-height: 1.35; }
  .contact__list { list-style: none; margin-top: 12px; font-size: 12px; color: var(--text-muted); line-height: 1.45; }
  .contact__list li { display: flex; align-items: center; gap: 8px; }
  .contact__icon { width: 10px; height: 10px; fill: none; stroke: var(--brand-blue); stroke-width: 1.6; }
  .wave { position: absolute; left: 0; top: 0; width: 560px; height: 320px; }
</style>
</head>
<body>
  <section class="card card--front">
    <div class="brand"><span class="brand__mark"></span>Veltor Group</div>
    <p class="website">www.veltorgroup.com</p>
  </section>

  <section class="card card--back">
    <svg class="wave" viewBox="0 0 560 320" aria-hidden="true">
      <path d="M0,276 C170,306 360,236 560,258 V320 H0 Z" fill="var(--band-grey)"/>
      <path d="M0,290 C170,314 360,246 560,266 V320 H0 Z" fill="var(--white)"/>
      <path d="M0,294 C170,318 360,250 560,270 V320 H0 Z" fill="var(--brand-blue)"/>
    </svg>

    <div class="brand"><span class="brand__mark"></span>Veltor Group</div>
    <div class="divider"></div>

    <div class="contact">
      <h1 class="contact__name">Daniel Harwood</h1>
      <p class="contact__role">Founder</p>
      <p class="contact__address">48 Corniche Tower Rd.<br>Business Bay, Dubai 00000</p>
      <ul class="contact__list">
        <li><svg class="contact__icon" viewBox="0 0 10 10"><path d="M2,1 L4,3 L3,4 C4,6 5,7 6,7 L7,6 L9,8 L8,9 C4,9 1,6 1,2 Z"/></svg>971-400-5512</li>
        <li><svg class="contact__icon" viewBox="0 0 10 10"><rect x="1" y="2" width="8" height="6"/><path d="M1,2 L5,5.5 L9,2"/></svg>info@veltorgroup.com</li>
        <li><svg class="contact__icon" viewBox="0 0 10 10"><circle cx="5" cy="5" r="4"/><path d="M1,5 H9 M5,1 C3,3.5 3,6.5 5,9 M5,1 C7,3.5 7,6.5 5,9"/></svg>www.veltorgroup.com</li>
      </ul>
    </div>
  </section>
</body>
</html>
```